Website Design for a Walking/Fitness Company
StrideNova.com
Website Design for a Walking/Fitness Company - Health
Creative Brief
Health
www.stridenova.example
The company is looking to build a new website with the domain name stridenova.example. We have just completed a logo project on here so have a new Logo to based the colours on. The website is based on effective walking. Miriam Cole has developed a system over many years of better walking. She delivers this training via online tutorials (available after logging in) and via 4 day camps based in the UK and abroad. The site needs to be clean and clear. The old site based on the domain miriamcole.example should not be used as a reference as it is dated and busy. The new site needs to deliver the message in a clear way. Also, the demographic is both male and female so please dont slant it either way
The client is keen on having a slider that has a video of her walking across the screen in slow motion. We have the video but we need the slider to handle it. The demographic ranges from 30 up 70 years old, so we would like the menu system across the top. The client has given the below websites as sites that they like but dont let it constrain your ideas. The main theme is that it needs to be clean and modern using the latest standards with a login feature. I would also suggest that under the slider (maybe on the right) there are smaller boxes highlighting the next camp. The site also has an ecommerce section. In terms of tabs/content use the old site miriamcole.example for reference. http://www.velmora.example/ https://www.harrietbloom.example/ http://uk.lumiroq.example/ Herewevo.example
Inspirational
The logo colours and black and green
top
http://www.velmora.example/
https://www.harrietbloom.example/
Herewevo.example
The logo for reference is here: http://www.quorbeldraft.example/contests/redesign-logo-brand-for-walking-excersize-website Please use the Green A as the reference. The client is looking to add more depth and colour into the green.. so maybe make the website in a more vibrant green. The existing site (miriamcole.example) has alot of content... and the new site needs to deliver a clean and clear message around key information
Concepts
Home Health International Web Template
Website Design for fun relationship

```html
<!DOCTYPE html>
<html lang="en">
<head>
<meta charset="utf-8">
<title>StrideNova – The Effective Walking System</title>
<link href="https://fonts.googleapis.com/css2?family=Lato:ital,wght@0,400;0,700;1,400&family=Play:wght@400;700&family=Exo+2:ital,wght@0,300;1,300&display=swap" rel="stylesheet">
<style>
:root{
  --green:#3fa535;
  --green-dark:#2f8a27;
  --green-text:#3aa534;
  --ink:#222;
  --text:#444;
  --grey-bg:#f2f2f2;
  --line:#d6d6d6;
  --black:#111;
  --footer:#1d1d1d;
  --footer-text:#d8d8d8;
}
*{margin:0;padding:0;box-sizing:border-box}
html,body{width:1200px;height:2430px;overflow:hidden;background:#fff}
body{position:relative;font-family:'Lato',sans-serif;color:var(--text);font-size:13px}
.abs{position:absolute}
a{color:inherit;text-decoration:none}
.play{font-family:'Play',sans-serif}
.g{color:var(--green-text)}

/* top bar */
.topbar{left:0;top:0;width:1200px;height:28px;background:var(--black);color:#eee;font-size:12.5px}
.topbar .call{left:132px;top:7px;display:flex;align-items:center;gap:6px}
.topbar .account{right:132px;top:6px;display:flex;gap:10px;align-items:center}
.topbar .account span+span{border-left:1px solid #555;padding-left:10px}

/* header */
.brand{left:132px;top:50px;display:flex;align-items:center;gap:10px}
.brand .dot{width:22px;height:22px;border-radius:50%;background:var(--green)}
.brand .name{font-family:'Lato',sans-serif;font-weight:700;font-size:38px;color:var(--black);letter-spacing:1px}
.search{left:799px;top:47px;width:270px;height:38px;border:1px solid #ccc;padding:12px;font-size:13px;color:#888}
.search svg{position:absolute;right:12px;top:12px}
.tagline{left:799px;top:101px;width:270px;text-align:right;font-family:'Exo 2',sans-serif;font-style:italic;font-weight:300;font-size:20px;color:#555}

/* nav */
.nav{left:0;top:144px;width:1200px;height:47px;background:var(--green)}
.nav ul{list-style:none;display:flex;position:absolute;left:143px;top:16px;gap:0;color:#fff;font-size:13px;font-weight:700}
.nav li{margin-right:31px}
.nav li:last-child{margin-right:0}

/* hero */
.hero{left:0;top:191px;width:1200px;height:524px;background:linear-gradient(160deg,#6f8a3a 0%,#a9b966 35%,#5b6b3a 60%,#8aa055 100%)}
.hero .msg{left:714px;top:170px;font-family:'Exo 2',sans-serif;font-weight:300;color:#fff;font-size:30px;line-height:36px}
.hero .msg b{color:#6ed64a;font-family:'Play',sans-serif;font-weight:400}
.hero .arrow{top:229px;width:64px;height:64px;border-radius:50%;border:2px solid rgba(255,255,255,.35)}
.dots{left:570px;top:486px;display:flex;gap:5px}
.dots i{width:11px;height:11px;border-radius:50%;background:rgba(255,255,255,.7)}
.dots i:first-child{background:transparent;border:2px solid #fff}

/* feature cards */
.card{top:754px;width:300px;height:187px;border:1px solid #d4d4d4;background:#f7f7f5;overflow:hidden}
.card h3{position:absolute;left:18px;top:11px;font-family:'Play',sans-serif;font-weight:700;font-size:20px;line-height:19px;color:var(--ink)}
.card h3 .g{display:block}
.card .photo{position:absolute;left:14px;top:57px;width:272px;height:94px}
.card .more{position:absolute;right:-1px;bottom:-1px;width:135px;height:32px;background:var(--green);border-top-left-radius:120px 40px;color:#fff;font-weight:700;font-size:13px;padding:10px 0 0 62px}

/* about */
.about{left:0;top:978px;width:1200px;height:318px;background:var(--grey-bg)}
.about h2{left:133px;top:36px;font-family:'Play',sans-serif;font-weight:700;font-size:27px;color:var(--ink)}
.about .rule{left:133px;top:77px;width:593px;height:1px;background:#bbb}
.about .lead{left:133px;top:91px;width:600px;font-weight:700;color:#222;font-size:14.5px;line-height:22.6px}
.about .body{left:133px;top:167px;width:600px;font-size:14.5px;line-height:22.6px;color:#444}
.btn{display:inline-block;background:var(--green);color:#fff;font-weight:700;font-size:15px;border:1px solid var(--green-dark);box-shadow:inset 0 -2px 0 rgba(0,0,0,.15)}
.about .btn{position:absolute;left:134px;top:251px;width:143px;height:29px;text-align:center;line-height:27px}
.about .portrait{left:772px;top:32px;width:245px;height:245px;border-radius:50%;border:4px solid var(--green);background:radial-gradient(circle at 50% 40%,#d7b59c,#9a8c87 60%,#4b5fc0 100%)}

/* services */
.services{left:0;top:1296px;width:1200px;height:380px;background:var(--green)}
.services h2{left:0;top:32px;width:1200px;text-align:center;font-family:'Play',sans-serif;font-weight:700;font-size:28px;color:#1f3a1b}
.services h2 span{color:#fff}
.services .rule{left:438px;top:77px;width:323px;height:1px;background:rgba(255,255,255,.5)}
.services .rule i{position:absolute;left:131px;top:-1px;width:61px;height:3px;background:#fff}
.svc{top:117px;width:200px;text-align:center;color:#fff;font-family:'Play',sans-serif;font-weight:700;font-size:19.5px;line-height:24px}
.svc .ph{width:160px;height:160px;margin:0 auto 14px;border-radius:50%;border:4px solid #2d7d26}

/* blog columns */
.col{top:1700px;width:283px}
.col h2{font-family:'Play',sans-serif;font-weight:700;font-size:27px;color:var(--ink);padding-bottom:10px;border-bottom:1px solid var(--line);position:relative}
.col h2::after{content:"";position:absolute;left:0;bottom:-2px;width:64px;height:3px;background:var(--green)}
.entry{padding:16px 0 14px;border-bottom:1px solid var(--line);font-size:13px;line-height:17.5px}
.entry:last-of-type{border-bottom:none}
.entry .date{color:var(--green-text);margin-right:14px}
.entry .ttl{color:var(--green-text);text-decoration:underline}
.entry p{margin-top:8px}
.entry .dots2{color:var(--green-text)}
.newsrow{display:flex;gap:18px}
.newsrow .thumb{width:64px;height:46px;flex:none;margin-top:6px;border:1px solid #ccc}
.col .btn{position:absolute;top:400px;padding:0 10px;height:29px;line-height:27px}
.testi .person{display:flex;align-items:center;gap:24px;margin-top:20px}
.testi .avatar{width:96px;height:96px;border-radius:50%;border:4px solid var(--green);background:linear-gradient(150deg,#6a8a4b,#d64a8c)}
.testi .who b{display:block;color:var(--green-text);font-size:15px}
.testi blockquote{margin-top:14px;font-style:italic;font-size:13.5px;line-height:20px;color:#444}
.testi .q{color:#8fcf84;font-size:30px;font-family:'Play',sans-serif;vertical-align:-8px}

/* footer */
.swoosh{left:0;top:1990px}
.footer{left:0;top:2138px;width:1200px;height:254px;background:var(--footer);color:var(--footer-text)}
.fcol{top:35px}
.fcol h4{font-weight:400;font-size:19px;color:#fff;padding-bottom:6px;border-bottom:1px solid #444;margin-bottom:10px}
.links{list-style:none;font-size:13px;line-height:19.7px}
.links li::before{content:"› ";color:#aaa}
.contact{font-size:13px;line-height:15.5px}
.contact .row{display:flex;gap:14px;margin-bottom:20px}
.contact svg{flex:none;margin-top:1px}
.news p{font-size:13px;line-height:16px;width:210px}
.news .field{margin-top:18px;width:208px;height:30px;background:#fff;color:#777;padding:7px 10px;font-size:13px}
.news .btn{margin-top:14px;padding:0 15px;height:29px;line-height:27px}
.fbrand{left:891px;top:70px;width:178px;text-align:center;font-weight:700;font-size:30px;color:#8a8a8a}
.copy{left:891px;top:207px;width:178px;text-align:center;font-size:13px;line-height:20px}
.bottombar{left:0;top:2392px;width:1200px;height:38px;background:#0e0e0e;color:#ddd;font-size:13px}
.bottombar .legal{left:133px;top:11px;display:flex}
.bottombar .legal span{padding:0 9px;border-left:1px solid #555}
.bottombar .legal span:first-child{padding-left:0;border:0}
.social{right:132px;top:12px;display:flex;gap:10px}
.social i{width:14px;height:14px;border-radius:50%;background:#ddd}
</style>
</head>
<body>

<div class="abs topbar">
  <div class="abs call">
    <svg width="13" height="13" viewBox="0 0 24 24"><path fill="#3fa535" d="M6.6 10.8a15.1 15.1 0 006.6 6.6l2.2-2.2a1 1 0 011-.25 11.4 11.4 0 003.6.57 1 1 0 011 1V20a1 1 0 01-1 1A17 17 0 013 4a1 1 0 011-1h3.5a1 1 0 011 1 11.4 11.4 0 00.57 3.6 1 1 0 01-.25 1z"/></svg>
    Any Questions? Call Us: <b>+44 (0)20 5550 0142</b>
  </div>
  <div class="abs account"><span>Member Login</span><span>Register</span></div>
</div>

<header>
  <div class="abs brand"><i class="dot"></i><span class="name">STRIDENOVA</span></div>
  <div class="abs search">Search
    <svg width="13" height="13" viewBox="0 0 16 16"><circle cx="6.5" cy="6.5" r="5" fill="none" stroke="#888" stroke-width="1.8"/><path d="M10 10l4.5 4.5" stroke="#888" stroke-width="1.8"/></svg>
  </div>
  <div class="abs tagline">The Effective Walking System</div>
</header>

<nav class="abs nav">
  <ul>
    <li>HOME</li><li>WHAT IS STRIDENOVA</li><li>SHOP</li><li>SUCCESSES</li><li>GALLERY</li><li>WHAT'S NEW</li><li>STRIDENOVA CLUB</li><li>PRESS</li><li>CONTACT</li>
  </ul>
</nav>

<section class="abs hero" role="img" aria-label="Slider photo: a family walking together along a sunny park path with their dog">
  <div class="abs msg">Get StrideNova today and<br><b>LOOK</b> better, <b>FEEL</b> better<br>and <b>PERFORM</b> better!</div>
  <div class="abs arrow" style="left:37px">
    <svg width="60" height="60" viewBox="0 0 60 60"><path d="M35 16L21 30l14 14" fill="none" stroke="#fff" stroke-width="2"/></svg>
  </div>
  <div class="abs arrow" style="left:1099px">
    <svg width="60" height="60" viewBox="0 0 60 60"><path d="M25 16l14 14-14 14" fill="none" stroke="#fff" stroke-width="2"/></svg>
  </div>
  <div class="abs dots"><i></i><i></i><i></i><i></i></div>
</section>

<section>
  <article class="abs card" style="left:131px">
    <h3><span class="g">Audio Coaching</span>Session</h3>
    <div class="photo" role="img" aria-label="Photo: woman training outdoors by a lake" style="background:linear-gradient(135deg,#8a9aa8,#b56a55 60%,#6b5a50)"></div>
    <span class="more">More ➔</span>
  </article>
  <article class="abs card" style="left:450px">
    <h3><span class="g">New 28 Days To Success</span>Online Programme!!</h3>
    <div class="photo" role="img" aria-label="Photo: woman exercising at home in front of a screen" style="background:linear-gradient(135deg,#f2f0ea,#d9dde2 55%,#4a78c8)"></div>
    <span class="more">More ➔</span>
  </article>
  <article class="abs card" style="left:769px">
    <h3><span class="g">StrideNova Next</span>Camp</h3>
    <div class="photo" role="img" aria-label="Photo: couple hiking with backpacks in the countryside" style="background:linear-gradient(135deg,#3e5a2e,#6b7a5a 50%,#e8762e)"></div>
    <span class="more">More ➔</span>
  </article>
</section>

<section class="abs about">
  <h2 class="abs">What is StrideNova? <span class="g">Get StrideNova!</span></h2>
  <div class="abs rule"></div>
  <p class="abs lead">StrideNova is the Effective Walking System created by Sport Scientist &amp; Diet &amp; Movement Specialist Miriam Cole. The aim of StrideNova is to make every step you take both effective and productive!</p>
  <p class="abs body">Walking is the most accessible form of physical activity for the vast majority of people, yet many of us are not reaping the benefits of our walking efforts, as we don’t use the right technique.</p>
  <span class="btn">Get StrideNova!</span>
  <div class="abs portrait" role="img" aria-label="Portrait photo of the founder in a blue top"></div>
</section>

<section class="abs services">
  <h2 class="abs">StrideNova <span>Services</span></h2>
  <div class="abs rule"><i></i></div>
  <div class="abs svc" style="left:143px"><div class="ph" role="img" aria-label="Photo: woman holding her shoulders" style="background:linear-gradient(135deg,#f5f5f5,#e2c4ad 60%,#7a5a40)"></div>Reduce Joint Stress</div>
  <div class="abs svc" style="left:380px"><div class="ph" role="img" aria-label="Photo: couple meditating outdoors" style="background:linear-gradient(135deg,#c9d6b5,#f0ece6 50%,#d7b59c)"></div>Improve Posture</div>
  <div class="abs svc" style="left:618px"><div class="ph" role="img" aria-label="Photo: measuring tape around a waist" style="background:linear-gradient(135deg,#f7f7f7,#e8c9b4 50%,#d8607a)"></div>Trim Waistline</div>
  <div class="abs svc" style="left:856px"><div class="ph" role="img" aria-label="Photo: oversized jeans after weight loss" style="background:linear-gradient(180deg,#f7f7f7,#e6c8b0 45%,#3f5f93)"></div>Lose Weight &amp; Improve<br>Your Body Shape</div>
</section>

<section>
  <div class="abs col" style="left:133px">
    <h2><span class="g">Recent</span> Blog</h2>
    <div class="entry"><span class="date">19.01.2014</span><span class="ttl">Technical Help</span>
      <p>Use this section to look through any support queries related to any technical issues on the website. <span class="dots2">[...]</span></p></div>
    <div class="entry"><span class="date">23.04.2015</span><span class="ttl">Walking Shoes</span>
      <p>Use this section to look through any queries you may have relating to our recomended range of walking shoes <span class="dots2">[...]</span></p></div>
    <span class="btn">More News</span>
  </div>

  <div class="abs col" style="left:463px">
    <h2><span class="g">What's</span> New?</h2>
    <div class="entry"><div class="newsrow"><span class="date" style="margin:0">01.01.2015</span><span class="ttl">Join our StrideNova Team - Job Vacancy for StrideNova Events</span></div>
      <div class="newsrow"><div class="thumb" role="img" aria-label="Photo: group at an event" style="background:linear-gradient(135deg,#3a4a6a,#c9cfd8)"></div><p>StrideNova is the Effective Walking System created by <span class="dots2">[...]</span></p></div></div>
    <div class="entry"><div class="newsrow"><span class="date" style="margin:0">01.01.2015</span><span class="ttl">StrideNova Camps 2015 &amp; 2016! More dates released</span></div>
      <div class="newsrow"><div class="thumb" role="img" aria-label="Photo: resort pool by the sea" style="background:linear-gradient(180deg,#5fa8e0,#27b7c2 60%,#e7e0cf)"></div><p>StrideNova Camps with Miriam Cole &amp; StrideNova team <span class="dots2">[...]</span></p></div></div>
    <span class="btn">More News</span>
  </div>

  <div class="abs col testi" style="left:790px">
    <h2><span class="g">Client</span> Testimonials</h2>
    <div class="person"><div class="avatar" role="img" aria-label="Photo of the client"></div>
      <div class="who"><b>Miss Lena Hartwig</b>Business Woman</div></div>
    <blockquote><span class="q">“</span> My name is Lena Hartwig, I am 46 years old, I'm from Germany and have never been particularly athletic. For jogging I lack the breath, I hate swimming and <span class="dots2" style="font-style:normal">[...]</span></blockquote>
    <span class="btn">Read More</span>
  </div>
</section>

<svg class="abs swoosh" width="1200" height="150" viewBox="0 0 1200 150">
  <path d="M0 62 C260 150 650 140 1200 28 L1200 150 L0 150 Z" fill="#1d1d1d"/>
  <path d="M0 18 C180 120 520 150 880 88 C700 128 260 130 0 48 Z" fill="#3fa535"/>
</svg>

<footer class="abs footer">
  <div class="abs fcol" style="left:133px;width:120px">
    <h4>Quick Links</h4>
    <ul class="links"><li>Home</li><li>What Is StrideNova</li><li>Shop</li><li>Successes</li><li>Gallery</li><li>What's New</li><li>StrideNova Club</li><li>Press</li><li>Contact</li></ul>
  </div>
  <div class="abs fcol contact" style="left:340px;width:184px">
    <h4>Contact Information</h4>
    <div class="row"><svg width="12" height="16" viewBox="0 0 12 16"><path d="M6 0a6 6 0 00-6 6c0 4.5 6 10 6 10s6-5.5 6-10a6 6 0 00-6-6zm0 8.5A2.5 2.5 0 116 3.5a2.5 2.5 0 010 5z" fill="#fff"/></svg><span>Miriam Cole StrideNova,<br>Lantern Studio,<br>18 Fernwick Lane,<br>London. N1 0ZZ</span></div>
    <div class="row"><svg width="14" height="14" viewBox="0 0 24 24"><path fill="#fff" d="M6.6 10.8a15.1 15.1 0 006.6 6.6l2.2-2.2a1 1 0 011-.25 11.4 11.4 0 003.6.57 1 1 0 011 1V20a1 1 0 01-1 1A17 17 0 013 4a1 1 0 011-1h3.5a1 1 0 011 1 11.4 11.4 0 00.57 3.6 1 1 0 01-.25 1z"/></svg><span>+44 (0)20 5550 0142</span></div>
    <div class="row"><svg width="14" height="14" viewBox="0 0 16 16"><rect x="4" y="1" width="8" height="4" fill="#fff"/><rect x="1" y="6" width="14" height="6" rx="1" fill="#fff"/><rect x="4" y="10" width="8" height="5" fill="#fff" stroke="#1d1d1d"/></svg><span>+44 (0)20 5550 0199</span></div>
    <div class="row"><svg width="14" height="11" viewBox="0 0 14 11"><rect width="14" height="11" fill="#fff"/><path d="M0 0l7 6 7-6" fill="none" stroke="#1d1d1d" stroke-width="1.2"/></svg><span>enquiries@miriamcole.example</span></div>
  </div>
  <div class="abs fcol news" style="left:607px;width:216px">
    <h4>Newsletter Sign Up</h4>
    <p>Sign up for Miriam's eNewsletters, packed with useful tips, advice and information on all our fantastic events and products.</p>
    <div class="field">Email Address</div>
    <span class="btn">Subscribe</span>
  </div>
  <div class="abs fbrand">StrideNova</div>
  <div class="abs copy">© Miriam Cole 2015.<br>All Right Reserved.</div>
</footer>

<div class="abs bottombar">
  <div class="abs legal"><span>Privacy Policy</span><span>Terms &amp; Condition</span><span>Unsubscribe</span></div>
  <div class="abs social"><i></i><i></i><i></i><i></i><i></i></div>
</div>

</body>
</html>
```